Package design for paper cups, bags and a sweets box (white or grey color)
I have logo designed.
name of brand (MARLOWEN)

Requirements
Should not have
• The color must be gray or white, and yellow and blue can be used

```html
<!DOCTYPE html>
<html lang="en">
<head>
<meta charset="utf-8">
<title>Marlowen Specialty Coffee – Cup Wrap</title>
<link href="https://fonts.googleapis.com/css2?family=Montserrat:wght@400;500&display=swap" rel="stylesheet">
<style>
  :root {
    --stage: #e9e9e9;
    --paper: #ecebe7;
    --splash: #b9babc;
    --ink: #a4a5a8;
    --sketch: #cfcfd0;
  }
  html, body {
    margin: 0;
    padding: 0;
    width: 1200px;
    height: 1000px;
    overflow: hidden;
    background: var(--stage);
  }
  .canvas {
    position: relative;
    width: 1200px;
    height: 1000px;
  }
  .cup-wrap {
    position: absolute;
    left: 240px;
    top: 100px;
    width: 720px;
    height: 800px;
    background: var(--paper);
    overflow: hidden;
  }
  .splash-area {
    position: absolute;
  }
  .splash-area-top {
    left: 0;
    top: 0;
    width: 480px;
    height: 300px;
    background: radial-gradient(ellipse at 0% 0%, var(--splash) 0%, var(--splash) 35%, rgba(185,186,188,0) 72%);
  }
  .splash-area-bottom {
    right: 0;
    bottom: 0;
    width: 260px;
    height: 220px;
    background: radial-gradient(ellipse at 100% 100%, var(--splash) 0%, var(--splash) 40%, rgba(185,186,188,0) 75%);
  }
  .brand {
    position: absolute;
    left: 0;
    right: 0;
    top: 270px;
    display: flex;
    flex-direction: column;
    align-items: center;
  }
  .brand-dot {
    width: 120px;
    height: 120px;
    border: 4px solid var(--ink);
    border-radius: 50%;
    box-sizing: border-box;
    margin-bottom: 34px;
  }
  .brand-name {
    font-family: "Montserrat", sans-serif;
    font-weight: 500;
    font-size: 62px;
    letter-spacing: 10px;
    color: var(--ink);
    margin: 0;
    padding-left: 10px;
    line-height: 1.1;
  }
  .brand-tagline {
    font-family: "Montserrat", sans-serif;
    font-weight: 500;
    font-size: 22px;
    letter-spacing: 5px;
    color: var(--ink);
    margin: 10px 0 0;
    padding-left: 5px;
  }
  .sketch {
    position: absolute;
    width: 34px;
    height: 34px;
    border-radius: 50%;
    background: var(--sketch);
  }
  .sketch-bean-left { left: 70px; top: 250px; }
  .sketch-plant-right { right: 50px; top: 440px; }
  .sketch-leaf-right { right: 70px; top: 520px; }
  .sketch-bean-right { right: 180px; top: 580px; }
</style>
</head>
<body>
  <main class="canvas">
    <section class="cup-wrap">
      <div class="splash-area splash-area-top" role="img" aria-label="Grey ink splash pattern along the top edge"></div>
      <div class="splash-area splash-area-bottom" role="img" aria-label="Grey ink splash pattern in the lower corner"></div>

      <div class="sketch sketch-bean-left" role="img" aria-label="Small line sketch of a coffee bean"></div>
      <div class="sketch sketch-plant-right" role="img" aria-label="Small line sketch of a coffee cherry branch"></div>
      <div class="sketch sketch-leaf-right" role="img" aria-label="Small line sketch of a coffee leaf"></div>
      <div class="sketch sketch-bean-right" role="img" aria-label="Small line sketch of a coffee bean"></div>

      <div class="brand">
        <div class="brand-dot"></div>
        <h1 class="brand-name">MARLOWEN</h1>
        <p class="brand-tagline">SPECIALTY COFFEE</p>
      </div>
    </section>
  </main>
</body>
</html>
```